Use your magic to make a startup company look established*

We are in need of a website that gives the appearance that we are established rather than new. Our audience is comprised of senior executives in technology professional services companies, financial people (conservative) that invest in them, and executives in companies that are in need of their services. The site therefore needs to lean towards the conservative side while being modern and professional.

This should be a fairly simple site.

- About us
- Services
- Contacts
- Content (Articles)

It should be SEO friendly and easy to add content or sub pages. A responsive design is mandatory.

Target Market(s)

We work with executives and investors in professional services companies to more effectively compete in the already crowded “digital transformation” market.

Industry/Entity Type

Professional Service

Coding

Coded - Design and coding required

Number of Pages Required

5+ page

Font styles to use
Sans Serif

Requirements
Must have
• - Responsive design
- Easy to add/change content
- Easy to add additional pages

```html
<!DOCTYPE html>
<html lang="en">
<head>
<meta charset="utf-8">
<title>Summit Crest Advisors</title>
<link href="https://fonts.googleapis.com/css2?family=Jost:wght@400;500;600&family=Montserrat:wght@500;600;700&family=Lato:wght@400;700&display=swap" rel="stylesheet">
<style>
:root{
  --gold:#bf8f3a;
  --gold-light:#d3a64c;
  --ink:#1c1c1c;
  --text:#555;
  --nav:#454545;
  --soft:#f3f2f2;
  --grey:#efefef;
  --footer:#252525;
  --copy:#3c3c3c;
}
*{box-sizing:border-box;margin:0;padding:0}
html,body{width:1200px;height:3463px;overflow:hidden}
body{position:relative;background:#fff;font-family:'Lato',sans-serif;color:var(--text)}
.abs{position:absolute}
.gold-btn{background:linear-gradient(180deg,var(--gold-light),var(--gold));color:#fff;font-family:'Montserrat',sans-serif;font-weight:600;display:flex;align-items:center;justify-content:center}
.eyebrow{font-family:'Jost',sans-serif;color:var(--gold);font-size:13px;text-transform:uppercase;letter-spacing:.3px}
.title{font-family:'Jost',sans-serif;font-weight:500;color:var(--ink);font-size:33px;line-height:1.1}
.center{left:0;width:1200px;text-align:center}
.read-more{font-family:'Montserrat',sans-serif;font-size:10px;font-weight:600;color:var(--gold)}

/* header */
.brand{left:122px;top:56px;display:flex;align-items:center;gap:10px}
.brand-dot{width:12px;height:12px;border-radius:50%;background:var(--gold)}
.brand-name{font-family:'Jost',sans-serif;font-size:19px;font-weight:500;color:#555;white-space:nowrap}
.header-contact{font-size:13px;line-height:1.35}
.header-contact .label{color:var(--gold);font-weight:700;font-size:12px;display:flex;gap:6px;align-items:center}
.header-contact .value{color:#333;padding-left:18px}
.social{display:flex;gap:4px}
.social span{width:18px;height:18px;background:#333;display:block}

/* nav */
.main-nav{left:0;top:123px;width:1200px;height:42px;background:var(--nav)}
.main-nav a{position:absolute;top:0;height:42px;line-height:42px;color:#fff;font-family:'Montserrat',sans-serif;font-size:12px;font-weight:600;text-decoration:none;transform:translateX(-50%)}
.main-nav a.active{color:var(--gold-light)}
.main-nav .cta{left:968px;width:166px;transform:none;text-align:center;background:var(--gold)}

/* hero */
.hero-visual{left:0;top:165px;width:1200px;height:511px;background:linear-gradient(100deg,#c9dce6 0%,#9fbccd 35%,#4a6b85 62%,#1d2e48 80%,#101a2d 100%)}
.hero-copy{left:105px;top:322px;width:450px}
.hero-copy h1{font-family:'Montserrat',sans-serif;font-weight:700;font-size:34px;line-height:33px;color:#111;width:480px}
.hero-copy p{margin-top:16px;font-size:11.5px;font-weight:700;color:#111;line-height:16px}
.hero-copy .gold-btn{margin-top:24px;width:148px;height:42px;font-size:13px}

/* about */
.about-text{left:125px;top:845px;width:940px;font-size:12.5px;line-height:15.5px;color:#666}
.about-text p+p{margin-top:15px}
.pill{left:540px;top:991px;width:108px;height:34px;border-radius:17px;font-size:9.5px;letter-spacing:.8px}

/* services */
.services-band{left:12px;top:1089px;width:1188px;height:444px;background:var(--soft)}
.lead{font-size:13px;line-height:20px;color:#555}
.service-col{width:290px}
.service-col h3{font-family:'Montserrat',sans-serif;font-size:14px;font-weight:700;color:var(--ink)}
.service-col p{margin-top:18px;font-size:12.5px;line-height:16px;color:#666}
.service-col .read-more{display:block;margin-top:18px}
.divider{width:1px;height:125px;background:#666}

/* team */
.portrait{width:192px;height:197px}
.member{width:260px;text-align:center}
.member h4{font-family:'Montserrat',sans-serif;font-size:13.5px;font-weight:700;color:var(--gold)}
.member span{display:block;margin-top:5px;font-size:12.5px;color:#666}

/* contact */
.contact-band{left:0;top:2076px;width:1200px;height:621px;background:var(--grey)}
.contact-title{font-family:'Jost',sans-serif;font-weight:600;font-size:32px;color:var(--ink);line-height:1}
.contact-info{font-size:12.5px;line-height:15px;color:#444}
.map{left:115px;top:2352px;width:467px;height:279px;background:linear-gradient(135deg,#9fc9a0 0%,#b8d4ad 40%,#e7e1c9 70%,#eae4d2 100%)}
.field-label{font-size:12.5px;color:#444}
.field{background:#fff;border:1px solid #b8b8b8;width:344px;height:32px}
.send{left:708px;top:2607px;width:125px;height:37px;background:var(--gold);color:#fff;font-size:13px;display:flex;align-items:center;justify-content:center}

/* articles */
.article{width:250px}
.article .meta{font-size:10px;color:#444}
.article h3{margin-top:14px;font-family:'Lato',sans-serif;font-weight:400;font-size:16px;line-height:19px;color:var(--gold)}
.article p{margin-top:16px;font-size:11.5px;line-height:15.5px;color:#777}
.article .read-more{display:block;margin-top:16px}

/* footer */
.site-footer{left:0;top:3124px;width:1200px;height:296px;background:var(--footer)}
.footer-brand{left:113px;top:3198px;display:flex;align-items:center;gap:8px}
.footer-brand .brand-dot{width:10px;height:10px}
.footer-brand .brand-name{font-size:15px;color:#ddd}
.footer-about{left:110px;top:3255px;width:275px;font-size:12px;line-height:15px;color:#ddd}
.footer-social{left:113px;top:3347px;display:flex;gap:4px}
.footer-social span{width:20px;height:20px;border:1px solid var(--gold);background:#b18327;display:block}
.footer-heading{font-family:'Montserrat',sans-serif;font-size:13px;font-weight:600;color:var(--gold-light)}
.quick-links{list-style:none}
.quick-links li{font-size:12px;color:#ddd;height:23.5px;display:flex;align-items:center;gap:12px}
.quick-links li::before{content:"";border-left:5px solid var(--gold);border-top:3px solid transparent;border-bottom:3px solid transparent}
.offer-list{list-style:none;width:155px}
.offer-list li{font-size:12px;color:#ddd;height:24.5px;line-height:22px;border-bottom:1px solid #bbb}
.offer-list li:last-child{border:none}
.footer-contact{font-size:12px;line-height:15px;color:#ddd}
.footer-contact .row{display:flex;gap:12px}
.copyright{left:0;top:3420px;width:1200px;height:43px;background:var(--copy);color:#ddd;font-size:12px;line-height:43px;text-align:center}
</style>
</head>
<body>

<header>
  <div class="abs brand">
    <div class="brand-dot"></div>
    <div class="brand-name">Summit Crest Advisors</div>
  </div>
  <div class="abs header-contact" style="left:414px;top:53px">
    <div class="label"><svg width="12" height="12" viewBox="0 0 24 24"><path fill="#bf8f3a" d="M6.6 10.8a15 15 0 0 0 6.6 6.6l2.2-2.2c.3-.3.7-.4 1-.2 1.1.4 2.3.6 3.6.6.6 0 1 .4 1 1V20c0 .6-.4 1-1 1A17 17 0 0 1 3 4c0-.6.4-1 1-1h3.5c.6 0 1 .4 1 1 0 1.3.2 2.5.6 3.6.1.3 0 .7-.2 1z"/></svg>Call Us Now</div>
    <div class="value" style="font-weight:700">+ (555) 204-3187</div>
  </div>
  <div class="abs header-contact" style="left:645px;top:53px">
    <div class="label"><svg width="12" height="10" viewBox="0 0 24 18"><rect width="24" height="18" fill="#bf8f3a"/><path d="M1 1l11 9 11-9" stroke="#fff" stroke-width="2" fill="none"/></svg>Contact Email</div>
    <div class="value" style="font-size:12px;color:#555">info@summitcrestadvisors.com</div>
  </div>
  <div class="abs" style="left:969px;top:50px">
    <div style="color:var(--gold);font-size:12px;font-weight:700;margin-bottom:4px">Follow Us</div>
    <div class="social"><span></span><span></span><span></span><span></span><span></span></div>
  </div>
</header>

<nav class="abs main-nav">
  <a class="active" href="#" style="left:153px">HOME</a>
  <a href="#" style="left:277px">ABOUT US</a>
  <a href="#" style="left:401px">SERVICES</a>
  <a href="#" style="left:533px">OUR TEAM</a>
  <a href="#" style="left:656px">BLOG</a>
  <a href="#" style="left:775px">CONTENT</a>
  <a href="#" style="left:896px">CONTACT US</a>
  <a class="cta" href="#">MAKE APPOINTMENT</a>
</nav>

<section>
  <div class="abs hero-visual" role="img" aria-label="Businessman holding a tablet with glowing financial charts and figures"></div>
  <div class="abs hero-copy">
    <h1>We help you Invest in technology professional services companies</h1>
    <p>At cum veri epicurei constituto, legendos maluisset ne vis. Nam nulla incorrupte id. In labore &nbsp;suscipit salutandi vix. Ne odio persius omittam cum</p>
    <div class="gold-btn">Contact us</div>
  </div>
</section>

<section>
  <div class="abs center eyebrow" style="top:745px">About Us</div>
  <h2 class="abs center title" style="top:762px">Welcome to Summit Crest Advisors</h2>
  <div class="abs about-text">
    <p>Lorem ipsum dolor sit amet, cu per porro dolore nostro, partem integre corpora per ea, tation ornatus mel ad. Brute voluptatibus an est, per cu utroque torquatos, ei eum amet hinc. Ne vix ludus timeam definitionem. His hinc dicunt minimum cu, qui te dico laoreet. Sea ea mucius diceret solens, eos ei nostrud appellantur, an autem vocent novum doctus id mel. Id everti commune accusata melsunt explicabo. Nemo enim ipsam voluptatem quia voluptas sit aspernatur aut odit aut fugit,</p>
    <p>sed quia consequuntur magni dolores eos qui ratione voluptatem sequi nesciunt. Neque porro quisquam est, qui dolorem ipsum quia dolor sit amet, consectetur, adipisci velit, sed quia non numquam eius modi tempora incidunt ut labore et dolore magnam aliquam</p>
  </div>
  <div class="abs gold-btn pill">READ MORE</div>
</section>

<section>
  <div class="abs services-band"></div>
  <div class="abs center eyebrow" style="top:1155px">Viderer nostrud an est</div>
  <h2 class="abs center title" style="top:1171px">Our Main Services</h2>
  <p class="abs lead" style="left:140px;top:1234px;width:960px;text-align:center">quo in errem diceret tincidunt. Usu te alii argumentum, vis ea platonem reprehendunt. Et liber nostrud temporibus mei, viderer nostrud an est. Splendide definitionem at pro. Ut sit putant legimus an viris scripta deterruisset sit. Ad movet labitur reprimique cum, no his qualisque consetetur.</p>
  <div class="abs service-col" style="left:117px;top:1342px">
    <h3>INVESTMENT SERVICES</h3>
    <p>Lorem ipsum dolor sit amet, consectetur adipiscing elit, sed do eiusmod tempor incididunt ut labore et vis ea platonem reprehendunt.</p>
    <span class="read-more">READ MORE</span>
  </div>
  <div class="abs divider" style="left:430px;top:1333px"></div>
  <div class="abs service-col" style="left:462px;top:1344px">
    <h3>FINANCIAL SERVICES</h3>
    <p>Lorem ipsum dolor sit amet, consectetur adipiscing elit, sed do eiusmod tempor incididunt ut labore et vis ea platonem reprehendunt.</p>
    <span class="read-more">READ MORE</span>
  </div>
  <div class="abs divider" style="left:777px;top:1333px"></div>
  <div class="abs service-col" style="left:803px;top:1343px">
    <h3>CUSTOMER SERVICES</h3>
    <p>Lorem ipsum dolor sit amet, consectetur adipiscing elit, sed do eiusmod tempor incididunt ut labore et vis ea platonem reprehendunt.</p>
    <span class="read-more">READ MORE</span>
  </div>
</section>

<section>
  <div class="abs center eyebrow" style="top:1591px">Nostrud an est</div>
  <h2 class="abs center title" style="top:1607px">Our Team</h2>
  <p class="abs" style="left:140px;top:1670px;width:920px;text-align:center;font-size:12.5px;line-height:15px;color:#666">At cum veri epicurei constituto, legendos maluisset ne vis. Nam nulla incorrupte id. In labore suscipit salutandi vix. Ne odio persius omittam cum. Iisque aliquam his ad.Velit liber graeci in eum, quo in errem diceret tincidunt. Usu te alii argumentum, at pro. Ut sit putant legimus, an viris scripta deterruisset sit. Ad movet labitur reprimique cum, no &nbsp;his qualisque consetetur</p>
  <div class="abs portrait" style="left:240px;top:1748px;background:linear-gradient(180deg,#cfd6dc,#8f9aa6 60%,#2a3548)" role="img" aria-label="Portrait of Daniel Mercer, CEO"></div>
  <div class="abs portrait" style="left:515px;top:1748px;background:linear-gradient(180deg,#a9a9a9,#8c8c8c 55%,#1f4f8a)" role="img" aria-label="Portrait of Claire Hollis, Founder"></div>
  <div class="abs portrait" style="left:794px;top:1748px;background:linear-gradient(180deg,#ececec,#d9d9d9 55%,#2c2c30)" role="img" aria-label="Portrait of Marcus Reed, Executive"></div>
  <div class="abs member" style="left:206px;top:1965px"><h4>DANIEL MERCER</h4><span style="margin-left:-24px">CEO</span></div>
  <div class="abs member" style="left:487px;top:1965px"><h4>CLAIRE HOLLIS</h4><span>Founder</span></div>
  <div class="abs member" style="left:759px;top:1965px"><h4>MARCUS REED</h4><span>Executives</span></div>
</section>

<section>
  <div class="abs contact-band"></div>
  <div class="abs eyebrow" style="left:122px;top:2158px">Viderer nostrud</div>
  <h2 class="abs contact-title" style="left:121px;top:2178px">Contact us</h2>
  <div class="abs contact-info" style="left:119px;top:2237px">Summit Crest Advisors<br>4120 Harbor Point Way, Lindale, USA</div>
  <div class="abs contact-info" style="left:119px;top:2284px">+ (555) 204-3187<br>info@summitcrestadvisors.com</div>
  <div class="abs map" role="img" aria-label="Road map showing the office location"></div>

  <div class="abs eyebrow" style="left:705px;top:2158px">Enquiry</div>
  <h2 class="abs contact-title" style="left:704px;top:2178px">Make Appointment</h2>
  <div class="abs field-label" style="left:708px;top:2236px">Name <sup>*</sup></div>
  <div class="abs field" style="left:708px;top:2260px"></div>
  <div class="abs field-label" style="left:708px;top:2307px">Email <sup>*</sup></div>
  <div class="abs field" style="left:708px;top:2331px"></div>
  <div class="abs field-label" style="left:708px;top:2380px">Subject</div>
  <div class="abs field" style="left:708px;top:2403px"></div>
  <div class="abs field-label" style="left:708px;top:2451px">Message</div>
  <div class="abs field" style="left:708px;top:2474px;width:347px;height:106px"></div>
  <div class="abs send">Send</div>
</section>

<section>
  <div class="abs center eyebrow" style="top:2750px">Ostrud an est</div>
  <h2 class="abs center title" style="top:2764px">Articles</h2>
  <p class="abs" style="left:146px;top:2826px;width:900px;font-size:12.5px;line-height:15px;color:#555">An hoc usque quaque, aliter in vita? Non igitur de improbo, sed de callido improbo quaerimus, qualis Q. Nam quibus rebus efficiuntur voluptates, eae non sunt in potestate sapientis. Negare non possum. Huic mori optimum esse propter desperationem sapientiae, illi propter spem vivere. Quid enim me prohiberet Epicureum esse, si probarem, quae ille diceret? Qui-vere falsone, quaerere mittimus-dicitur oculis se privasse</p>
  <article class="abs article" style="left:148px;top:2893px">
    <div class="meta">By Admin | 4 January 2021</div>
    <h3>Lorem ipsum dolor sit amet cu per porro dolore nostro</h3>
    <p>Lorem ipsum dolor sit amet, cu per porro dolore nostro, partem integre corpora per ea, tation ornatus mel ad Brute voluptati-</p>
    <span class="read-more">READ MORE</span>
  </article>
  <article class="abs article" style="left:458px;top:2899px">
    <div class="meta">By Admin | 4 January 2021</div>
    <h3>Sum dolor sit amet cu per porro dolore nostro</h3>
    <p>Lorem ipsum dolor sit amet, cu per porro dolore nostro, partem integre corpora per ea, tation ornatus mel ad Brute voluptati-</p>
    <span class="read-more">READ MORE</span>
  </article>
  <article class="abs article" style="left:784px;top:2899px">
    <div class="meta">By Admin | 4 January 2021</div>
    <h3>Porro dolore nostro Lorem ipsum dolor sit ametcu per</h3>
    <p>Lorem ipsum dolor sit amet, cu per porro dolore nostro, partem integre corpora per ea, tation ornatus mel ad Brute voluptati-</p>
    <span class="read-more">READ MORE</span>
  </article>
</section>

<footer>
  <div class="abs site-footer"></div>
  <div class="abs footer-brand">
    <div class="brand-dot"></div>
    <div class="brand-name">Summit Crest Advisors</div>
  </div>
  <p class="abs footer-about">Lorem ipsum dolor sit amet, cu per porro dolore nostro, partem integre corpora per ea, tation ornatus mel ad. Brute voluptatibus an est, per cu utroque torquatos, ei eum amet hinc.</p>
  <div class="abs footer-social"><span></span><span></span><span></span><span></span><span></span></div>

  <div class="abs footer-heading" style="left:457px;top:3181px">Quick Link</div>
  <ul class="abs quick-links" style="left:457px;top:3215px">
    <li>About us</li><li>Services</li><li>Our Team</li><li>Blog</li><li>Content</li><li>Contact us</li>
  </ul>

  <div class="abs footer-heading" style="left:644px;top:3181px">What We do</div>
  <ul class="abs offer-list" style="left:644px;top:3213px">
    <li>Epicurei constituto</li><li>Legendos maluisset</li><li>Usu te alii argumentum</li><li>Labitur reprimique</li><li>Dolorum adolescens</li><li>Discere antiopam</li>
  </ul>

  <div class="abs footer-heading" style="left:869px;top:3181px">Contact info</div>
  <div class="abs footer-contact" style="left:870px;top:3222px">
    <div class="row"><svg width="11" height="14" viewBox="0 0 24 32"><path fill="#bf8f3a" d="M12 0a12 12 0 0 0-12 12c0 9 12 20 12 20s12-11 12-20A12 12 0 0 0 12 0zm0 17a5 5 0 1 1 0-10 5 5 0 0 1 0 10z"/></svg><span>Summit Crest Advisors<br>4120 Harbor Point Way<br>Lindale, USA</span></div>
    <div class="row" style="margin-top:24px"><svg width="12" height="12" viewBox="0 0 24 24"><path fill="#bf8f3a" d="M6.6 10.8a15 15 0 0 0 6.6 6.6l2.2-2.2c.3-.3.7-.4 1-.2 1.1.4 2.3.6 3.6.6.6 0 1 .4 1 1V20c0 .6-.4 1-1 1A17 17 0 0 1 3 4c0-.6.4-1 1-1h3.5c.6 0 1 .4 1 1 0 1.3.2 2.5.6 3.6.1.3 0 .7-.2 1z"/></svg><span style="font-weight:700">+ (555) 204-3187</span></div>
    <div class="row" style="margin-top:15px"><svg width="12" height="10" viewBox="0 0 24 18"><rect width="24" height="18" fill="#bf8f3a"/><path d="M1 1l11 9 11-9" stroke="#252525" stroke-width="2" fill="none"/></svg><span>info@summitcrestadvisors.com</span></div>
  </div>
  <div class="abs copyright">Copyright 2020, Summit Crest Advisors, All Right Reserved</div>
</footer>

</body>
</html>
```